Postcard Design for Birchfield Medical Center Integrated Medicine

We need a postcard that we will be able to hand out at events that gives an overview of what we do at Birchfield Medical Center. Birchfield Medical Center, located in Encinitas, California, is an integrated medical center using functional medicine to prevent and reverse chronic diseases. We would also like to highly emphasize that we take Medicare and PPO insurance for these services and if patients have any questions to contact the front desk.

The attached screenshots are elementary versions of what we hope our postcard will have.

THIS IS NOT INTENDED TO BE MAILED SO AN ADDRESS SPACE IS NOT NEEDED
ALSO, WE WOULD LIKE TO HAVE THIS SIZE 6X4

Birchfieldmedcenter.net is our website if you would need any further information about the company.

```html
<!DOCTYPE html>
<html lang="en">
<head>
<meta charset="utf-8">
<title>Birchfield Medical Center – Postcard</title>
<link href="https://fonts.googleapis.com/css2?family=Exo+2:ital,wght@0,600;1,500;1,600;1,700&family=Arimo:ital,wght@0,400;0,700;1,400&display=swap" rel="stylesheet">
<style>
  :root{
    --teal:#19a3c2;
    --teal-deep:#12a7a6;
    --teal-band:#1ca8c6;
    --grey-text:#6f6f6f;
    --footer-bg:#ececec;
    --tick:#e2312f;
    --white:#ffffff;
  }
  *{box-sizing:border-box;margin:0;padding:0}
  html,body{width:1200px;height:1000px;overflow:hidden;background:#fff}
  body{position:relative;font-family:"Arimo",Arial,sans-serif}

  .card{position:absolute;background:var(--white);box-shadow:0 2px 10px rgba(0,0,0,.28);overflow:hidden}
  .card--front{left:16px;top:16px;width:762px;height:509px;z-index:2}
  .card--back{left:413px;top:465px;width:764px;height:508px;z-index:1}

  /* front */
  .brand{position:absolute;left:62px;top:48px;display:flex;align-items:center;gap:10px;
    font-family:"Exo 2",sans-serif;font-weight:600;font-size:22px;color:var(--teal);line-height:1.1;width:240px}
  .brand__mark{width:22px;height:22px;border-radius:50%;background:var(--teal);flex:none}
  .headline{position:absolute;left:336px;top:34px;font-family:"Exo 2",sans-serif;font-style:italic;font-weight:600;
    font-size:29px;line-height:32px;color:var(--teal)}
  .hero{position:absolute;left:0;top:121px;width:762px;height:305px;
    background:linear-gradient(100deg,#6e6a52 0%,#4b5a3c 22%,#3a3a38 40%,#cfcfcb 62%,#9aa687 80%,#4f6a3a 100%)}
  .hero__shade{position:absolute;inset:0;background:radial-gradient(circle at 30% 45%,rgba(0,0,0,.25),transparent 60%)}
  .hero__copy{position:absolute;left:62px;top:60px;width:312px;font-family:"Exo 2",sans-serif;font-weight:600;
    font-size:14.5px;line-height:19.5px;color:var(--white)}
  .hero__wave{position:absolute;left:0;bottom:-1px;width:762px;height:60px}
  .contact{position:absolute;left:60px;top:399px;color:var(--teal)}
  .contact__name{font-size:15px;line-height:16.5px}
  .contact__doctor{font-size:15.5px;margin-top:9px}
  .contact__address{color:var(--grey-text);font-size:14px;line-height:17px;margin-top:8px}
  .reach{position:absolute;right:56px;top:458px;text-align:right;color:var(--grey-text)}
  .reach__web{font-style:italic;font-size:13px}
  .reach__call{font-size:14.5px;margin-top:10px}
  .reach__phone{color:var(--teal);font-weight:700;margin-left:8px}

  /* back */
  .sky{position:absolute;left:0;top:0;width:764px;height:190px;
    background:linear-gradient(180deg,#b9a9d3 0%,#c9b7dc 30%,#b8b0d6 60%,#cfc6e2 100%)}
  .sky__glow{position:absolute;inset:0;background:radial-gradient(circle at 88% 8%,rgba(255,248,225,.95),transparent 40%)}
  .tagline{position:absolute;left:30px;top:71px;font-family:"Exo 2",sans-serif;font-style:italic;font-weight:600;
    font-size:23px;line-height:30px;color:var(--white)}
  .band{position:absolute;left:0;top:150px;width:764px;height:300px}
  .program{position:absolute;left:30px;top:207px;width:228px;color:var(--white);font-size:14.6px;line-height:15.7px}
  .conditions{position:absolute;left:300px;top:175px;width:440px;color:var(--white)}
  .conditions__title{font-family:"Exo 2",sans-serif;font-style:italic;font-weight:500;font-size:16px;line-height:20px;text-align:right;padding-right:10px}
  .conditions__cols{display:flex;margin-top:14px;margin-left:14px}
  .conditions__list{list-style:none;width:210px;font-size:10px}
  .conditions__list li{position:relative;height:13.2px;line-height:13.2px;padding-left:12px;white-space:nowrap}
  .conditions__list li::before{content:"";position:absolute;left:2px;top:2px;width:3px;height:6px;
    border-right:1.5px solid var(--tick);border-bottom:1.5px solid var(--tick);transform:rotate(45deg)}
  .insurance{position:absolute;left:0;top:447px;width:764px;height:61px;background:var(--footer-bg);
    text-align:center;color:var(--grey-text);font-style:italic;font-size:15.5px;line-height:19px;padding-top:10px}
</style>
</head>
<body>

<section class="card card--back" aria-label="Postcard back">
  <div class="sky" role="img" aria-label="Photo of soft pastel clouds lit by the sun"><div class="sky__glow"></div></div>
  <h2 class="tagline">Treating Root Causes Not Symptoms,<br>Creating Optimal Health and Vitality</h2>
  <svg class="band" viewBox="0 0 764 300" preserveAspectRatio="none" aria-hidden="true">
    <path d="M0 28 C120 16 230 10 300 16 L300 300 L0 300Z" fill="var(--teal-deep)"/>
    <path d="M287 16 C420 30 560 10 764 0 L764 300 L287 300Z" fill="var(--teal-band)"/>
  </svg>
  <p class="program">Our new specialized, therapeutic lifestyle program called <strong>RootWell Therapy (RWT).</strong> is very different from today's common medical approach. The RWT program works to more clearly identify and overcome the cause of ill health, and then improve total body function naturally by nourishing, balancing and revitalizing the whole individual. It is powerful, effective, and rewards you with improved health and function that</p>
  <div class="conditions">
    <h3 class="conditions__title">Some of the conditions we treat are:</h3>
    <div class="conditions__cols">
      <ul class="conditions__list">
        <li>Acne</li><li>Alzheimer's disease and Dementia</li><li>Arthritis</li><li>Asthma</li>
        <li>Autism Spectrum Disorder, ADD, ADHD</li><li>Autoimmune Diseases</li><li>Cancer Prevention</li>
        <li>Chronic Fatigue</li><li>Chronic Sinusitis</li><li>Depression and Anxiety</li><li>Detoxification and Healing</li>
        <li>Diabetes</li><li>Digestive Disorders</li><li>Eczema/Psoriasis</li><li>Elevated Cholesterol</li>
        <li>Environmental and Food Allergies</li><li>Fatigue</li>
      </ul>
      <ul class="conditions__list">
        <li>Female Disorders</li><li>Fibromyalgia</li><li>Healthy Aging</li><li>Healthy Weight and Metabolism</li>
        <li>Heart Health</li><li>Hormone Balance</li><li>Interstitial Cystitis</li><li>Mercury and Heavy Metal Toxicity</li>
        <li>Metabolic Syndrome,</li><li>Pre-Diabetes, Insulin Resistance</li><li>Migraines and Headaches</li>
        <li>MS (Multiple Sclerosis)</li><li>Osteoporosis</li><li>Parkinson's disease</li><li>Restless Leg Syndrome</li>
        <li>Sleep/Insomnia</li><li>Thyroid and Adrenal Disorders</li><li>And many more</li>
      </ul>
    </div>
  </div>
  <p class="insurance">We accept all Medicare and PPO insurance<br>Please contact the front desk for more information</p>
</section>

<section class="card card--front" aria-label="Postcard front">
  <div class="brand"><span class="brand__mark"></span><span>Birchfield Medical Center</span></div>
  <h1 class="headline">Mind, Body, Spirit:<br>Healing the Whole Person</h1>
  <div class="hero" role="img" aria-label="Spa still life photo with stacked black stones, white candles, pink bath salt and a purple orchid">
    <div class="hero__shade"></div>
    <p class="hero__copy">Holistic medicine called lifestyle functional medicine. Treating root causes not symptoms using a whole system approach to<br>healing chronic disease and creating optimal health and vitality.</p>
    <svg class="hero__wave" viewBox="0 0 762 60" preserveAspectRatio="none" aria-hidden="true">
      <path d="M0 60 L0 38 C90 8 200 6 320 22 C470 42 600 50 762 40 L762 60Z" fill="var(--white)"/>
    </svg>
  </div>
  <div class="contact">
    <p class="contact__name">Birchfield Medical Center<br>Integrated Medicine</p>
    <p class="contact__doctor">Dr. Maren Ellsworth, M.D. ABAARM</p>
    <p class="contact__address">418 Harbor View Road, Suite 110<br>Westmere, CA 90817</p>
  </div>
  <div class="reach">
    <p class="reach__web">www.birchfieldmedcenter.net</p>
    <p class="reach__call">CALL US: <span class="reach__phone">555 632-0148</span></p>
  </div>
</section>

</body>
</html>
```